Innovative WordPress for a non-profit organization dedicated to providing healthcare to the less for

Bright Harbor Aid is a small non-profit organization. BHA's core mission is to provide free medical and dental care to the less fortunate. Aside from providing healthcare, BHA also helps build infrastructure such as orphanage, cancer centers, water wells and small homes for the homeless. As a non-profit, BHA has been sponsoring various social programs to help those in need. From building infrastructure to health care and most recently micro-finance, the BHA team is helping to GIve Back to the community at person at a time.

BHA is growing and needs help to restructure for the future. The corporate website design is the first step in a new branding strategy for the company.

BHA current website is divided into three specific target areas:
1. Mission: This area is dedicated to provide information about medical and dental mission hosted by BHA.

2. Infrastructure. This area is dedicated to provide information about infrastructure programs supported and completed by the BHA team. The projects includes orphanage, cancer centers. water wells, micro-finance, small homes for the homeless...etc.

3. Special Projects. This area is used to showcase specific short term projects which might come up.

Aside from the specific three target area, BHA also needs a NEWS area where news about BHA can be published.

Please put your thinking cape on and help produce the next generation WordPress template for Bright Harbor Aid. Your design will great enhance the level of volunteers recruited and also increase the level of help that BHA can provide for other.

For a quick glance at the BHA website today, please visit http://www.bhaexample.org. The BHA team is looking for a fresh design.

Thank you very much for taking the time to help BHA advance its mission of helping those in need.

Reason: Seeking more variety in design. Design needs to have a donate button, sponsors area, news, welcome message, 3 primary functions (mission, infrastructure, and specials projects). The BHA logo is available. Please note, you have the option to NOT use the colors associated with BHA logo. Thank you for helping with designing the new site.

Non-Profit

Requirements
Must have
• 1. Donate Now button.
2. Primary focus areas: MISSION / INFRASTRUCTURE / SPECIAL PROJECTS
3. News & Events
4. Welcome Message area
5. Sponsors area - place to add sponsor logos

Nice to have
• 1. Photo of the Month: Used to show a specific photo to represent events or functions completed by the BHA team.

Please show sample of one level down. For example, what does the page look like when I click the MISSION link.

```html
<!DOCTYPE html>
<html lang="en">
<head>
<meta charset="utf-8">
<title>Bright Harbor Aid</title>
<link rel="stylesheet" href="https://fonts.googleapis.com/css2?family=Open+Sans:ital,wght@0,400;0,600;0,700;0,800;1,400&display=swap">
<style>
:root{
  --green:#5fb547;
  --ink:#333;
  --muted:#8a8a8a;
  --line:#e3e3e3;
  --band:#f4f4f4;
  --foot:#2a2a2a;
  --foot-text:#9a9a9a;
  --foot-line:#3c3c3c;
  --tweet:#3aa6dd;
  --white:#fff;
}
*{box-sizing:border-box;margin:0;padding:0}
html,body{width:1200px;height:2184px;overflow:hidden}
body{position:relative;background:var(--white);font-family:"Open Sans",Arial,sans-serif;color:var(--ink)}
.topbar{position:absolute;top:0;left:0;width:1200px;height:28px;font-size:11px;color:var(--muted);text-align:right;padding:8px 100px 0 0}
.site-header{position:absolute;top:28px;left:0;width:1200px;height:132px}
.brand{position:absolute;left:40px;top:20px;display:flex;align-items:center;gap:12px}
.brand-mark{width:34px;height:34px;border-radius:50%;background:var(--green)}
.brand-name{font-size:30px;font-weight:800;color:var(--green);letter-spacing:.5px}
.main-nav{position:absolute;left:400px;top:92px;display:flex;gap:28px;font-size:12px;color:#555}
.main-nav span:first-child{color:var(--green)}
.search-icon{position:absolute;right:30px;top:94px}
.hero{position:absolute;top:160px;left:0;width:1200px;height:440px;background:linear-gradient(120deg,#7a8a96 0%,#b8b4ac 40%,#d9d3c6 60%,#8c8378 100%)}
.hero-caption{position:absolute;left:120px;top:120px;width:960px;padding:22px 34px;background:rgba(40,40,40,.55);color:var(--white)}
.hero-caption h1{font-size:32px;font-weight:700;line-height:1.2}
.hero-caption p{font-size:15px;margin-top:10px;line-height:1.45}
.hero-arrow{position:absolute;top:223px}
.hero-dots{position:absolute;bottom:16px;left:0;width:100%;display:flex;justify-content:center;gap:8px}
.hero-dots i{width:9px;height:9px;border-radius:50%;background:rgba(255,255,255,.6)}
.hero-dots i:first-child{background:var(--white)}
.team{position:absolute;top:600px;left:0;width:1200px;height:580px}
.section-title{text-align:center;font-size:26px;font-weight:700;letter-spacing:.5px;margin-top:64px}
.title-rule{width:60px;height:2px;background:var(--green);margin:10px auto 0}
.section-sub{text-align:center;font-size:12px;color:var(--muted);font-style:italic;margin-top:12px}
.team-grid{position:absolute;top:200px;left:100px;display:flex;gap:40px}
.member{width:220px;text-align:center}
.member-photo{width:220px;height:248px;background:linear-gradient(180deg,#ececec,#cfd3d8)}
.member h3{font-size:14px;font-weight:600;margin-top:18px}
.member .role{font-size:11px;color:var(--muted);margin-top:4px}
.member p{font-size:11px;color:var(--muted);line-height:1.6;margin-top:10px;padding:0 8px}
.featured{position:absolute;top:1180px;left:0;width:1200px;height:532px;background:var(--band)}
.featured::before{content:"";position:absolute;top:0;left:100px;width:1000px;height:1px;background:var(--line)}
.device-mockup{position:absolute;left:100px;top:150px;width:380px;height:210px;background:linear-gradient(160deg,#d8dde2,#aeb6bf);border-radius:6px}
.featured-text{position:absolute;left:568px;top:62px;width:540px}
.featured-text h2{font-size:22px;font-weight:700}
.featured-text .section-sub{text-align:left;margin-top:8px}
.feature-cols{display:flex;gap:20px;margin-top:20px}
.feature-cols ul{list-style:none;width:170px}
.feature-cols li.head{font-weight:700;color:var(--ink)}
.feature-cols li.head::before{display:none}
.feature-cols li{font-size:11px;color:#666;margin-bottom:10px;display:flex;align-items:center;gap:8px}
.feature-cols li::before{content:"";flex:none;width:7px;height:7px;border-radius:50%;background:var(--green)}
.btn{display:inline-block;background:var(--green);color:var(--white);font-size:11px;font-weight:700;padding:9px 22px;border-radius:2px;margin-top:12px;letter-spacing:.5px}
.sponsors{position:absolute;left:100px;top:420px;width:1000px;display:flex;align-items:center;gap:22px}
.sponsors h4{font-size:12px;font-weight:700;letter-spacing:.5px;width:110px}
.sponsors i{width:130px;height:54px;background:#e4e4e4;border:1px solid #dadada}
.site-footer{position:absolute;top:1712px;left:0;width:1200px;height:472px;background:var(--foot);color:var(--foot-text);font-size:11px}
.foot-brand{position:absolute;left:100px;top:60px;width:220px}
.foot-brand .brand{position:static}
.foot-brand .brand-name{font-size:30px}
.foot-brand p{line-height:1.7}
.foot-col{position:absolute;top:80px}
.foot-col h4{color:var(--white);font-size:13px;font-weight:700;margin-bottom:20px}
.contact-list li{list-style:none;display:flex;gap:10px;align-items:flex-start;margin-bottom:14px;line-height:1.5}
.socials{display:flex;gap:10px;margin-top:18px}
.socials i{width:22px;height:22px;background:var(--foot-line);border-radius:2px}
.tweet{display:flex;gap:10px;margin-bottom:18px;line-height:1.6}
.tweet-dot{flex:none;width:16px;height:16px;border-radius:50%;background:var(--tweet);margin-top:2px}
.tweet a{color:var(--tweet);text-decoration:none}
.field{width:180px;height:28px;background:#3a3a3a;border:1px solid #484848;margin-bottom:10px;padding:6px 8px;color:#888}
.field.message{height:80px}
.send{background:var(--green);color:var(--white);font-weight:700;font-size:11px;padding:7px 20px;display:inline-block}
</style>
</head>
<body>
<div class="topbar">support@bhaexample.org &nbsp;|&nbsp; Phone: +001 555 0142</div>

<header class="site-header">
  <div class="brand"><span class="brand-mark"></span><span class="brand-name">Bright Harbor Aid</span></div>
  <nav class="main-nav"><span>Home</span><span>About us</span><span>Mission</span><span>Special Projects</span><span>Infrastructure</span><span>Donate</span></nav>
  <svg class="search-icon" width="14" height="14" viewBox="0 0 14 14"><circle cx="6" cy="6" r="4.5" fill="none" stroke="#5fb547" stroke-width="1.6"/><line x1="9.3" y1="9.3" x2="13" y2="13" stroke="#5fb547" stroke-width="1.6"/></svg>
</header>

<section class="hero" role="img" aria-label="Photo of volunteer doctors at the clinic">
  <div class="hero-caption">
    <h1>Dr. Lena Hart, Dr. Mai Rowan and Clara Vesey</h1>
    <p>Dr. Lena Hart, Dr. Mai Rowan and Clara Vesey volunteering at the Bright Harbor Aid Clinic located at Quiet Pine Community Hall, Lakeview, CA on May 17, 2014</p>
  </div>
  <svg class="hero-arrow" style="left:16px" width="20" height="34" viewBox="0 0 20 34"><polyline points="16,3 4,17 16,31" fill="none" stroke="#fff" stroke-width="3"/></svg>
  <svg class="hero-arrow" style="right:16px" width="20" height="34" viewBox="0 0 20 34"><polyline points="4,3 16,17 4,31" fill="none" stroke="#fff" stroke-width="3"/></svg>
  <div class="hero-dots"><i></i><i></i><i></i></div>
</section>

<section class="team">
  <h2 class="section-title">OUR AWESOME TEAM</h2>
  <div class="title-rule"></div>
  <p class="section-sub">Welcome to Bright Harbor Aid: free medical and dental care, giving back one person at a time</p>
  <div class="team-grid">
    <article class="member"><div class="member-photo" role="img" aria-label="Portrait of team member"></div><h3>Nora Ellis</h3><div class="role">Medical Director</div><p>Leads our free medical clinics and recruits volunteer doctors for every mission day.</p></article>
    <article class="member"><div class="member-photo" role="img" aria-label="Portrait of team member"></div><h3>Owen Pryce</h3><div class="role">Infrastructure Lead</div><p>Oversees water wells, orphanage builds and small homes for families in need.</p></article>
    <article class="member"><div class="member-photo" role="img" aria-label="Portrait of team member"></div><h3>Felix Marsh</h3><div class="role">Team Leader</div><p>Guides our volunteers and keeps every program focused on giving back.</p></article>
    <article class="member"><div class="member-photo" role="img" aria-label="Portrait of team member"></div><h3>Adam Wren</h3><div class="role">Special Projects</div><p>Runs short term projects, from micro-finance to cancer center support.</p></article>
  </div>
</section>

<section class="featured">
  <div class="device-mockup" role="img" aria-label="Website shown on desktop and tablet screens"></div>
  <div class="featured-text">
    <h2>Our Featured Projects and Mission</h2>
    <p class="section-sub">Three ways we help: medical missions, lasting infrastructure and special projects.</p>
    <div class="feature-cols">
      <ul><li class="head">Mission</li><li>Free Medical Clinics</li><li>Free Dental Care</li><li>Health Screenings</li><li>Volunteer Doctors</li></ul>
      <ul><li class="head">Infrastructure</li><li>Orphanages</li><li>Cancer Centers</li><li>Water Wells</li><li>Homes for the Homeless</li></ul>
      <ul><li class="head">Special Projects</li><li>Micro-finance</li><li>Disaster Relief</li><li>School Supplies</li><li>Photo of the Month</li></ul>
    </div>
    <span class="btn">DONATE NOW</span>
  </div>
  <div class="sponsors">
    <h4>OUR SPONSORS</h4>
    <i></i><i></i><i></i><i></i><i></i><i></i>
  </div>
</section>

<footer class="site-footer">
  <div class="foot-brand">
    <div class="brand"><span class="brand-mark"></span><span class="brand-name">BHA</span></div>
    <p style="margin-top:40px">Bright Harbor Aid is a small non-profit providing free medical and dental care to the less fortunate.</p>
    <p style="margin-top:14px">We also build wells, orphanages and homes for those in need.</p>
  </div>

  <div class="foot-col" style="left:360px;width:240px">
    <h4>CONTACT INFO</h4>
    <ul class="contact-list">
      <li><svg width="12" height="14" viewBox="0 0 12 14"><path d="M6 1a4 4 0 0 1 4 4c0 3-4 8-4 8S2 8 2 5a4 4 0 0 1 4-4z" fill="#9a9a9a"/></svg>12 Harbor Lane, Springfield<br>Lakeview 3000</li>
      <li><svg width="12" height="12" viewBox="0 0 12 12"><rect x="1" y="2" width="10" height="8" fill="none" stroke="#9a9a9a"/><polyline points="1,2 6,7 11,2" fill="none" stroke="#9a9a9a"/></svg>info@bhaexample.org</li>
      <li><svg width="12" height="12" viewBox="0 0 12 12"><path d="M2 1h3l1 3-2 1a7 7 0 0 0 3 3l1-2 3 1v3c-6 0-9-3-9-9z" fill="#9a9a9a"/></svg>Phone: +001 555 0142</li>
    </ul>
    <div class="socials"><i></i><i></i><i></i><i></i><i></i><i></i></div>
  </div>

  <div class="foot-col" style="left:652px;width:230px">
    <h4>NEWS &amp; EVENTS</h4>
    <div class="tweet"><span class="tweet-dot"></span><p>New clinic day scheduled for the spring season, volunteers welcome <a>http://bhaexample.org/n1</a></p></div>
    <div class="tweet"><span class="tweet-dot"></span><p>Water well project reaches its second village this month <a>http://bhaexample.org/n2</a></p></div>
    <div class="tweet"><span class="tweet-dot"></span><p>Thank you to every donor who joined us <a>http://bhaexample.org/n3</a></p></div>
  </div>

  <div class="foot-col" style="left:928px;width:180px">
    <h4>DROP US A LINE!</h4>
    <div class="field">Name</div>
    <div class="field">Email Address</div>
    <div class="field message">Message</div>
    <span class="send">SEND</span>
  </div>
</footer>
</body>
</html>
```